zQuandaro Marketing - SEM, Influencer website. FUN RETRO VIBES.

I included content. Need an advertising website that displays, my services, blog and about me and contact.
I need to be able to easily update content, blogs by myself. Need it to be a Wordpress. I included some content pages. Please let me know if this give a better idea of what I do and the tone I am looking for.
Target Market(s)
Small Business Entrepreneurs, Start-ups, Male and Female ages 25-50
Industry/Entity Type
Advertising
Coding
Coded - Design and coding required
Number of Pages Required
3 page
Font styles to use
Other font styles liked:
- Lazer 64
Requirements
Must have
- Services, Blog, About Me, Contact. Creative Design is really what I want. Unique and fun imagery. I like the 80's style of design. Retro colors, in the logo. LAzer 84 font is cool. Hex colors should be in the brief. MUST LOOK GOOD ON MOBILE. The mobile experience has to be good.
Nice to have
- I am open minded to new creative ideas.
Hex Code
#000205
#3978A3
#5BF8FB
#7B7BFB
#5CC9EC
#AB63FA
Should not have
- Cookie Cutter feel. They made me choose the color wheel but the colors I want are on the brief. Please let me know if you need more logo images, images of me

```html
<!DOCTYPE html>
<html lang="en">
<head>
<meta charset="utf-8">
<title>zQuandaro World</title>
<link href="https://fonts.googleapis.com/css2?family=Teko:wght@300;400&family=Lato:wght@400;700&display=swap" rel="stylesheet">
<style>
:root{
  --ink:#000205;
  --steel:#3978A3;
  --cyan:#5BF8FB;
  --periwinkle:#7B7BFB;
  --sky:#5CC9EC;
  --violet:#AB63FA;
  --navy:#160f63;
  --deep-purple:#3a1e8a;
  --pale:#e8f3fa;
  --text-grey:#555a66;
  --white:#ffffff;
}
*{box-sizing:border-box;margin:0;padding:0}
html,body{width:1200px;height:4532px;overflow:hidden}
body{position:relative;background:var(--white);font-family:"Lato",sans-serif;color:var(--ink)}
.abs{position:absolute}
.display{font-family:"Teko",sans-serif;font-weight:300;letter-spacing:1px;line-height:1}

/* header */
.site-header{left:0;top:0;width:1200px;height:160px;background:var(--ink);z-index:3}
.brand{left:72px;top:22px;display:flex;align-items:center;gap:14px}
.brand-dot{width:60px;height:60px;border-radius:50%;border:2px solid var(--periwinkle)}
.brand-name{font-family:"Teko",sans-serif;font-weight:300;font-size:34px;color:var(--periwinkle);letter-spacing:1px}
.main-nav a{position:absolute;top:40px;font-family:"Teko",sans-serif;font-weight:300;font-size:22px;color:var(--white);text-decoration:none;transform:translateX(-50%);white-space:nowrap}
.main-nav a.active{color:var(--sky);border-bottom:1px solid var(--sky);padding-bottom:2px}

/* hero */
.hero{left:0;top:160px;width:1200px;height:620px;background:linear-gradient(180deg,#05051c 0%,#1a0f4a 30%,#5a1f8c 55%,#2f3aa8 78%,#3a9fd6 100%)}
.hero-title{left:0;top:172px;width:1200px;text-align:center;font-size:72px;color:var(--sky);z-index:2}
.hero-sub{left:0;top:244px;width:1200px;text-align:center;font-size:42px;color:var(--white);z-index:2}
.hero-arrow{top:356px;z-index:2}

/* about */
.about-photo-ring{left:98px;top:816px;width:392px;height:392px;border-radius:50%;padding:8px;background:linear-gradient(135deg,var(--sky),var(--violet))}
.about-photo{width:100%;height:100%;border-radius:50%;border:6px solid var(--white);background:linear-gradient(160deg,#cfd6e0,#8f9aa8 60%,#5f6875)}
.about-title{left:549px;top:842px;font-size:64px;background:linear-gradient(90deg,var(--steel),var(--violet));-webkit-background-clip:text;background-clip:text;-webkit-text-fill-color:transparent}
.about-hello{left:549px;top:924px;font-size:20px;color:var(--text-grey)}
.about-copy{left:549px;top:964px;width:550px;font-size:14.5px;line-height:27px;color:var(--text-grey)}
.btn-outline{left:544px;top:1127px;width:178px;height:52px;border:3px solid var(--periwinkle);border-radius:26px;color:var(--periwinkle);font-weight:700;font-size:16px;letter-spacing:.5px;display:flex;align-items:center;justify-content:center}

/* how it works */
.how{left:0;top:1296px;width:1200px;height:1110px;background:linear-gradient(180deg,#120b5e 0%,#1a1270 55%,#28229a 100%)}
.city-haze{left:0;top:1880px;width:1200px;height:480px;background:linear-gradient(180deg,transparent,rgba(60,70,170,.45))}
.section-title{width:1200px;left:0;text-align:center;font-size:52px;color:var(--white)}
.timeline-line{left:601px;top:1482px;width:0;height:820px;border-left:3px dashed var(--violet)}
.node{width:28px;height:28px;border-radius:50%;border:4px solid var(--sky);background:var(--navy);left:588px}
.step-box{border:1px solid var(--violet);background:rgba(20,12,90,.55);padding:24px 34px}
.step-box h3{font-family:"Teko",sans-serif;font-weight:300;font-size:48px;line-height:1;color:var(--violet);margin-bottom:6px}
.step-box.plan h3{color:var(--sky)}
.step-box p{font-size:14px;line-height:26px;color:var(--white)}
.step-art{width:200px;height:200px;border-radius:50%;background:radial-gradient(circle,rgba(123,123,251,.35),rgba(123,123,251,0) 70%)}
.top-btn{left:580px;top:2292px;width:46px;height:46px;border-radius:50%;background:var(--sky);display:flex;align-items:center;justify-content:center}

/* services */
.services{left:0;top:2366px;width:1200px;height:730px;background:linear-gradient(100deg,#5a1fb8 0%,#4a2bb0 45%,#2f6aa8 80%,#3a8aaa 100%)}
.services-grid{left:0;top:2860px;width:1200px;height:230px;background:linear-gradient(180deg,transparent,rgba(171,99,250,.55))}
.service-label{font-family:"Teko",sans-serif;font-weight:300;font-size:30px;color:var(--white);white-space:nowrap;transform:translateX(-50%)}
.service-icon{transform:translateX(-50%)}

/* blogs */
.blogs{left:0;top:3089px;width:1200px;height:570px;background:var(--pale)}
.blogs-title{color:var(--deep-purple)}
.blog-card{width:330px;text-align:center;transform:translateX(-50%)}
.blog-ring{width:236px;height:236px;margin:0 auto;border-radius:50%;padding:6px;background:linear-gradient(135deg,var(--sky),var(--violet))}
.blog-photo{width:100%;height:100%;border-radius:50%;border:5px solid var(--white);background:linear-gradient(150deg,#8aa0b8,#3b4a60 60%,#1d2535)}
.blog-date{margin-top:22px;font-size:15px;color:var(--violet)}
.blog-heading{margin-top:4px;font-size:18px;font-weight:400;line-height:24px;color:#222}
.blog-excerpt{margin-top:8px;font-size:12px;line-height:19px;color:#444}
.blog-link{margin-top:6px;font-size:13px;font-weight:700;color:var(--steel);letter-spacing:.5px}

/* contact */
.contact{left:0;top:3640px;width:1200px;height:690px;background:linear-gradient(180deg,#2a5f9e 0%,#2f7fb8 45%,#4bc4e2 80%,var(--cyan) 100%)}
.contact-title{left:123px;top:3780px;font-size:56px;color:var(--white)}
.contact-item{left:123px;display:flex;gap:22px;color:var(--white)}
.contact-item .label{font-size:17px;line-height:26px}
.contact-item .value{font-size:17px;line-height:28px}
.field{left:581px;width:461px;border-bottom:1px solid rgba(255,255,255,.8);color:var(--white);font-size:16px;padding-bottom:18px}
.btn-submit{left:583px;top:4094px;width:178px;height:54px;border-radius:27px;background:#0a0d2a;color:var(--white);font-weight:700;font-size:16px;letter-spacing:.5px;display:flex;align-items:center;justify-content:center}

/* footer */
.site-footer{left:0;top:4321px;width:1200px;height:211px;background:var(--ink)}
.footer-mark{left:556px;top:4279px;width:84px;height:84px;border-radius:50%;background:var(--ink);border:3px solid var(--periwinkle)}
.footer-nav a{position:absolute;top:4382px;font-family:"Teko",sans-serif;font-weight:300;font-size:22px;color:var(--white);text-decoration:none;transform:translateX(-50%);white-space:nowrap}
.copyright{left:0;top:4426px;width:1200px;text-align:center;font-size:13px;color:var(--white)}
.social{top:4463px;width:34px;height:34px;border-radius:50%;border:2px solid var(--periwinkle);transform:translateX(-50%)}
</style>
</head>
<body>

<!-- hero -->
<div class="abs hero" role="img" aria-label="Hero artwork: retro synthwave landscape"></div>
<svg class="abs" style="left:0;top:640px;z-index:2" width="1200" height="140" viewBox="0 0 1200 140">
  <defs><linearGradient id="edge" x1="0" x2="1"><stop offset="0" stop-color="#7B7BFB"/><stop offset="1" stop-color="#5BF8FB"/></linearGradient></defs>
  <path d="M0 130 L150 118 L330 100 L420 88 L500 60 L550 40 L590 70 L660 78 L760 92 L900 110 L1060 104 L1200 96 L1200 140 L0 140Z" fill="#fff"/>
  <path d="M0 130 L150 118 L330 100 L420 88 L500 60 L550 40 L590 70 L660 78 L760 92 L900 110 L1060 104 L1200 96" fill="none" stroke="url(#edge)" stroke-width="4"/>
</svg>

<header class="abs site-header">
  <div class="abs brand"><span class="brand-dot"></span><span class="brand-name">zQuandaro World</span></div>
  <nav class="main-nav">
    <a class="active" style="left:491px" href="#">HOME</a>
    <a style="left:593px" href="#">ABOUT ME</a>
    <a style="left:709px" href="#">SERVICES</a>
    <a style="left:811px" href="#">BLOGS</a>
    <a style="left:910px" href="#">WHY US</a>
    <a style="left:1027px" href="#">CONTACT US</a>
  </nav>
</header>

<h1 class="abs display hero-title">WELCOME TO zQUANDARO WORLD</h1>
<p class="abs display hero-sub">ZQUANDARO MARKETING EXPERT</p>
<svg class="abs hero-arrow" style="left:56px" width="26" height="40" viewBox="0 0 26 40"><path d="M20 4 L6 20 L20 36" fill="none" stroke="#fff" stroke-width="5"/></svg>
<svg class="abs hero-arrow" style="left:1120px" width="26" height="40" viewBox="0 0 26 40"><path d="M6 4 L20 20 L6 36" fill="none" stroke="#fff" stroke-width="5"/></svg>

<!-- about -->
<section>
  <div class="abs about-photo-ring"><div class="about-photo" role="img" aria-label="Portrait photo of the founder"></div></div>
  <h2 class="abs display about-title">ABOUT ME</h2>
  <p class="abs about-hello">Hello, Young visionaries!</p>
  <p class="abs about-copy">I am excited to tell you more about myself and the journey that brought me to this point. I am the founder and CEO of zQuandaro Marketing an organization that I created to share my knowledge and expertise in digital advertising. I have worked exclusively in the digital marketing arena for over 10 years and have gained valuable information throughout the process.</p>
  <div class="abs btn-outline">LEARN MORE</div>
</section>

<!-- how it works -->
<section>
  <div class="abs how"></div>
  <div class="abs city-haze" role="img" aria-label="Faint city skyline silhouette"></div>
  <h2 class="abs display section-title" style="top:1356px">HOW IT WORKS</h2>
  <div class="abs timeline-line"></div>
  <div class="abs node" style="top:1468px"></div>
  <div class="abs node" style="top:1741px"></div>
  <div class="abs node" style="top:2043px"></div>

  <div class="abs step-box" style="left:187px;top:1438px;width:359px;height:229px">
    <h3>VISUALIZE</h3>
    <p>zQuandaro verb pronounced [ z -kwan-dah-roh], or digital visionary is a person who uses the Internet as a global marketplace to release their ideas, products, and services to the world.</p>
  </div>
  <div class="abs step-box plan" style="left:690px;top:1718px;width:359px;height:229px">
    <h3>PLAN</h3>
    <p>Creating digital sales funnel for your business is key to your online growth. Each channel should work cohesively together to reach your target audience.</p>
  </div>
  <div class="abs step-box" style="left:192px;top:2001px;width:359px;height:229px">
    <h3>EXECUTE</h3>
    <p>Now that your plan is in place let's get ready to implement. Creating a campaign should be geared around conversion goals that were put in place during the planning stage.</p>
  </div>

  <div class="abs step-art" style="left:730px;top:1440px" role="img" aria-label="Line illustration of a person with a telescope and rising arrows"></div>
  <div class="abs step-art" style="left:280px;top:1720px" role="img" aria-label="Line illustration of a hand planning strategy on a screen"></div>
  <div class="abs step-art" style="left:715px;top:2010px" role="img" aria-label="Line illustration of a lightbulb inside a gear"></div>

  <div class="abs top-btn"><svg width="18" height="12" viewBox="0 0 18 12"><path d="M2 10 L9 3 L16 10" fill="none" stroke="#160f63" stroke-width="3"/></svg></div>
</section>

<!-- services -->
<section>
  <div class="abs services"></div>
  <svg class="abs" style="left:0;top:2366px" width="1200" height="90" viewBox="0 0 1200 90"><path d="M0 0 L1200 0 L1200 20 L0 84Z" fill="#5CC9EC"/></svg>
  <div class="abs services-grid" role="img" aria-label="Neon wireframe grid floor"></div>
  <svg class="abs" style="left:0;top:3020px" width="1200" height="76" viewBox="0 0 1200 76"><path d="M0 76 L1200 0 L1200 76Z" fill="#e8f3fa"/><path d="M1060 20 L1200 0 L1200 44Z" fill="#AB63FA"/></svg>
  <h2 class="abs display section-title" style="top:2474px">ADVERTISING SERVICES</h2>

  <svg class="abs" style="left:383px;top:2528px" width="400" height="400" viewBox="0 0 400 400">
    <defs><radialGradient id="glow"><stop offset="0" stop-color="#c04cf0"/><stop offset=".7" stop-color="#8a2fd6"/><stop offset="1" stop-color="#8a2fd6" stop-opacity="0"/></radialGradient></defs>
    <circle cx="200" cy="200" r="180" fill="url(#glow)" opacity=".6"/>
    <circle cx="200" cy="200" r="170" fill="none" stroke="#fff" stroke-width="2"/>
    <circle cx="200" cy="200" r="138" fill="none" stroke="#fff" stroke-width="3" opacity=".8"/>
    <g fill="#fff">
      <circle cx="71" cy="87" r="10"/><circle cx="328" cy="87" r="10"/>
      <circle cx="55" cy="280" r="10"/><circle cx="344" cy="280" r="10"/>
      <circle cx="200" cy="370" r="10"/>
    </g>
  </svg>

  <svg class="abs service-icon" style="left:390px;top:2570px" width="44" height="48" viewBox="0 0 44 48" fill="none" stroke="#fff" stroke-width="2"><circle cx="22" cy="20" r="11"/><path d="M17 32h10M18 38h8M22 2v4M6 8l3 3M38 8l-3 3"/></svg>
  <div class="abs service-label" style="left:290px;top:2626px">CAMPAIGN MANAGEMENT</div>
  <svg class="abs service-icon" style="left:776px;top:2568px" width="52" height="52" viewBox="0 0 52 52" fill="none" stroke="#fff" stroke-width="2"><rect x="20" y="4" width="28" height="20"/><circle cx="12" cy="26" r="6"/><path d="M2 50V38h20v12"/></svg>
  <div class="abs service-label" style="left:848px;top:2626px">EMPLOYEE TRAINING</div>
  <svg class="abs service-icon" style="left:378px;top:2785px" width="52" height="46" viewBox="0 0 52 46" fill="none" stroke="#fff" stroke-width="2"><rect x="4" y="4" width="44" height="28"/><path d="M26 32v10M16 44h20"/><circle cx="18" cy="16" r="5"/><path d="M32 12l8 8M40 12l-8 8"/></svg>
  <div class="abs service-label" style="left:313px;top:2838px">PLANNING &amp; PROPOSAL</div>
  <svg class="abs service-icon" style="left:788px;top:2783px" width="56" height="50" viewBox="0 0 56 50" fill="none" stroke="#fff" stroke-width="2"><rect x="22" y="2" width="32" height="18"/><circle cx="12" cy="14" r="6"/><circle cx="30" cy="28" r="5"/><path d="M2 48V30h18v18M22 48V38h16v10"/></svg>
  <div class="abs service-label" style="left:869px;top:2838px">ONE ON ONE CONSULTING</div>
  <svg class="abs service-icon" style="left:583px;top:2920px" width="50" height="50" viewBox="0 0 50 50" fill="none" stroke="#fff" stroke-width="2"><rect x="2" y="10" width="36" height="36"/><path d="M8 40V32M16 40V26M24 40V30M32 40V22M8 18h20"/><circle cx="40" cy="10" r="7"/></svg>
  <div class="abs service-label" style="left:583px;top:2976px">SEM SERVICES</div>
</section>

<!-- blogs -->
<section>
  <div class="abs blogs"></div>
  <h2 class="abs display section-title blogs-title" style="top:3108px">RECENT BLOGS</h2>
  <article class="abs blog-card" style="left:257px;top:3191px">
    <div class="blog-ring"><div class="blog-photo" role="img" aria-label="Photo of a man working at a laptop"></div></div>
    <p class="blog-date">25 FEB 2020</p>
    <h3 class="blog-heading">Curabitur vel mi sit amet<br>magna malesuada</h3>
    <p class="blog-excerpt">Arabitur vel dolor ultrices ipsum dictum<br>tristique Praesent vitae lacus</p>
    <p class="blog-link">LEARN MORE</p>
  </article>
  <article class="abs blog-card" style="left:609px;top:3191px">
    <div class="blog-ring"><div class="blog-photo" style="background:linear-gradient(150deg,#dfe6ee,#8e9fb4 60%,#3a4a62)" role="img" aria-label="Photo of a team reviewing documents at a table"></div></div>
    <p class="blog-date">15 FEB 2020</p>
    <h3 class="blog-heading">Curabitur vel mi sit amet<br>magna malesuada</h3>
    <p class="blog-excerpt">Arabitur vel dolor ultrices ipsum dictum<br>tristique Praesent vitae lacus</p>
    <p class="blog-link">LEARN MORE</p>
  </article>
  <article class="abs blog-card" style="left:961px;top:3191px">
    <div class="blog-ring"><div class="blog-photo" style="background:linear-gradient(150deg,#6a7486,#2a3040 60%,#10141e)" role="img" aria-label="Photo of hands typing on a keyboard"></div></div>
    <p class="blog-date">05 FEB 2020</p>
    <h3 class="blog-heading">Curabitur vel mi sit amet<br>magna malesuada</h3>
    <p class="blog-excerpt">Arabitur vel dolor ultrices ipsum dictum<br>tristique Praesent vitae lacus</p>
    <p class="blog-link">LEARN MORE</p>
  </article>
</section>

<!-- contact -->
<section>
  <div class="abs contact" role="img" aria-label="Blue gradient with faint city skyline and neon grid"></div>
  <svg class="abs" style="left:0;top:3636px" width="1200" height="100" viewBox="0 0 1200 100"><path d="M0 0 L1200 0 L1200 40 L0 4Z" fill="#e8f3fa"/><path d="M900 70 L1200 20 L1200 50Z" fill="#5CC9EC"/></svg>
  <h2 class="abs display contact-title">CONTACT US</h2>

  <div class="abs contact-item" style="top:3870px">
    <svg width="26" height="36" viewBox="0 0 26 36"><path d="M13 1C6 1 1 6 1 13c0 9 12 22 12 22s12-13 12-22C25 6 20 1 13 1z" fill="#fff"/><circle cx="13" cy="13" r="5" fill="#2f7fb8"/></svg>
    <div><p class="label">OUR ADDRESS</p><p class="value">482 Neon Grid Avenue, Suite 8, Austin TX 70000</p></div>
  </div>
  <div class="abs contact-item" style="top:3963px">
    <svg width="28" height="30" viewBox="0 0 28 30"><path d="M6 2l6 6-3 4c2 4 5 7 9 9l4-3 6 6-4 4C13 28 2 17 2 6z" fill="none" stroke="#fff" stroke-width="2.5"/></svg>
    <div><p class="label">PHONE NUMBER</p><p class="value">(555) 014 8084</p></div>
  </div>
  <div class="abs contact-item" style="top:4056px">
    <svg width="32" height="24" viewBox="0 0 32 24"><rect x="1" y="3" width="30" height="20" fill="#fff"/><path d="M1 3l15 11L31 3" fill="none" stroke="#2f7fb8" stroke-width="2"/></svg>
    <div><p class="label">EMAIL ADDRESS</p><p class="value">hello@zquandaro.test</p></div>
  </div>

  <div class="abs field" style="top:3820px">Your Name</div>
  <div class="abs field" style="top:3878px">Email address</div>
  <div class="abs field" style="top:3936px">Phone Number</div>
  <div class="abs field" style="top:3994px;padding-bottom:56px">Message</div>
  <div class="abs btn-submit">SUBMIT NOW</div>
</section>

<!-- footer -->
<footer>
  <div class="abs site-footer"></div>
  <div class="abs footer-mark"></div>
  <nav class="footer-nav">
    <a style="left:328px" href="#">HOME</a>
    <a style="left:430px" href="#">ABOUT ME</a>
    <a style="left:545px" href="#">SERVICES</a>
    <a style="left:648px" href="#">BLOGS</a>
    <a style="left:746px" href="#">WHY US</a>
    <a style="left:864px" href="#">CONTACT US</a>
  </nav>
  <p class="abs copyright">© 2020 Company Name | All Rights Reserved | Disclaimer</p>
  <span class="abs social" style="left:544px"></span>
  <span class="abs social" style="left:585px"></span>
  <span class="abs social" style="left:626px"></span>
  <span class="abs social" style="left:667px"></span>
</footer>

</body>
</html>
```